Business Card Design for a Technology Development Company

******* PLEASE NOTE (ALL DESIGNERS): I am going to finish the competition on Monday the 9th July (NOT SATURDAY 15TH). I have some designs I like and need to get them printed next week. Please submit any designs today or tomorrow. *******

PLEASE READ ALL OF THE REQUIREMENTS!!! I've rejected lot's of designs in the past because they didn't read the basic requirements - thanks and good luck!

Quill Harbor is a UK technology / small holding company that invests in startups and develops new ideas. In addition it provides IT Professional Services.

Ideally the design will be simple, professional, smart, and sophisticated, and overall be nice to look at. You can be creative as you like with the design, equally as simple as you like - you guys are the professionals so I'll leave it to your inspiration (make sure you incorporate the logo)!
Updates

PLEASE NOTE (ALL DESIGNERS): I am going to finish the competition on Monday the 9th July (NOT SATURDAY 15TH).  I have some designs I like and need to get them printed next week.  Please submit any designs today or tomorrow.

Target Market(s)

Enterprises / corporations / public sector / technical engineers / investors. More www.brontavex.com / www.pelmora.com than www.flinkaro.com!

Industry/Entity Type

Business

Requirements
Must have
• It should be modern and any artwork (if used) should be simple
- Pastel colours, dark and light colours, and shades are preferred over bright colours
- The design should incorporate the attached Quill Harbor logo and the logo colour scheme
- The logo should be on both sides. The back should just have the logo, maybe with some additional graphics
- It must have the following information on:

FirstName SecondName
Company Position
Email: name@quillharbor.co.uk
Mobile: +44 (0) 7700 900482

- The final design should be for a UK business card, dimensions: 85mm × 55mm
- The final design should have bleed marks to allow for printing and should be given in vector formats (EPS and AI)
Nice to have
• The Logo can be separated from the font in the logo on the front of the card. This isn't necessary or required, just to know it's not a limitation.
Should not have
• No bright colours (I prefer pastel colours, dark and light colours, and shades)
- Fonts that are to thin
- Effects or designs that make it difficult to print
- Italic or old fashioned looking fonts, i.e. anything like Times New Roman is a NO!

```html
<!DOCTYPE html>
<html lang="en">
<head>
<meta charset="utf-8">
<title>Quill Harbor – Business Card</title>
<link rel="stylesheet" href="https://fonts.googleapis.com/css2?family=Mulish:wght@400;600;700;800&display=swap">
<style>
  :root {
    --stage: #2f2f2f;
    --card: #ffffff;
    --teal: #0e7b87;
    --teal-deep: #16707b;
    --teal-light: #7cc3cc;
    --ink-soft: #d9eef0;
    --white: #ffffff;
  }
  * { box-sizing: border-box; margin: 0; padding: 0; }
  html, body {
    width: 1200px; height: 903px; overflow: hidden;
    background: var(--stage);
    font-family: "Mulish", sans-serif;
  }
  .stage { position: relative; width: 1200px; height: 903px; }
  .card {
    position: absolute;
    width: 484px; height: 313px;
    background: var(--card);
    overflow: hidden;
    box-shadow: 0 6px 18px rgba(0,0,0,0.35);
  }
  .card--front { left: 170px; top: 95px; }
  .card--back  { left: 546px; top: 480px; }

  /* front */
  .brand {
    position: absolute; left: 74px; top: 92px;
    display: flex; align-items: center; gap: 14px;
  }
  .brand__dot { width: 40px; height: 40px; border-radius: 50%; background: var(--teal-deep); }
  .brand__name { font-size: 40px; font-weight: 700; color: var(--teal-deep); letter-spacing: -0.5px; }
  .brand-url {
    position: absolute; right: 40px; top: 146px;
    font-size: 15px; color: var(--teal-light);
  }
  .brand-url strong { font-weight: 700; }
  .band {
    position: absolute; left: 0; right: 0; bottom: 0;
    background: var(--teal);
  }
  .card--front .band { height: 86px; }
  .holder { position: absolute; left: 44px; top: 20px; color: var(--white); }
  .holder__name { font-size: 14px; font-weight: 800; }
  .holder__role { font-size: 12px; font-weight: 400; margin-top: 3px; color: var(--ink-soft); }
  .contact {
    position: absolute; left: 230px; top: 20px;
    display: grid; grid-template-columns: auto auto; column-gap: 12px; row-gap: 4px;
    font-size: 12px; color: var(--white);
  }
  .contact dt { font-weight: 800; }
  .contact dd { font-weight: 400; color: var(--ink-soft); }

  /* back */
  .card--back .band { height: 140px; }
  .back-brand {
    position: absolute; left: 0; right: 0; top: 62px;
    display: flex; justify-content: center; align-items: center; gap: 12px;
  }
  .back-brand__dot { width: 30px; height: 30px; border-radius: 50%; background: var(--teal-deep); }
  .back-brand__name { font-size: 28px; font-weight: 700; color: var(--teal-deep); }
  .back-url {
    position: absolute; left: 0; right: 0; bottom: 52px;
    text-align: center; font-size: 15px; color: var(--white);
  }
  .back-url strong { font-weight: 800; }
</style>
</head>
<body>
<main class="stage">
  <section class="card card--front" aria-label="Business card front">
    <div class="brand">
      <span class="brand__dot"></span>
      <span class="brand__name">Quill Harbor</span>
    </div>
    <p class="brand-url"><strong>quillharbor</strong>.co.uk</p>
    <div class="band">
      <div class="holder">
        <p class="holder__name">Rhea Tanvold</p>
        <p class="holder__role">Graphic Designer</p>
      </div>
      <dl class="contact">
        <dt>Email</dt><dd>rhea@quillharbor.co.uk</dd>
        <dt>Mobile</dt><dd>+44 (0) 7700 900482</dd>
      </dl>
    </div>
  </section>

  <section class="card card--back" aria-label="Business card back">
    <div class="back-brand">
      <span class="back-brand__dot"></span>
      <span class="back-brand__name">Quill Harbor</span>
    </div>
    <div class="band">
      <p class="back-url" style="position:absolute;bottom:52px;"><strong>quillharbor</strong>.co.uk</p>
    </div>
  </section>
</main>
</body>
</html>
```